Design some Business Cards for free coaching services

Super easy project-- I'm building a holistic coaching practice (helping people to realize their dreams) and I'm giving away free intro sessions and want to have business cards to hand out as a way to spread the word-->help more people!

Side 1 of the card will have one of three designs (described below)
Side 2 of the card will have some basic text and maybe a small icon (or photo of me?)

Side 1: Design requests: for each of the 3 designs below have the top word (in all caps) take up the majority of the card, with the second line smaller and symmetrical with the above line... I'm not sure if this would be best on a solid color or with some kind of imagery... that's where your creativity comes in :) ~ though I'm attaching a photo I took of a card that I like that inspired this idea (biz card sample).

Design 1:
DISCOVER
your heart's deepest calling

Design 2:
TRANSFORM
limiting patterns and beliefs

Design 3:
MANIFEST
your highest potential

Side 2: Will have the following text with some kind of matching color scheme to Side 1 and possible a matching image or my headshot (see 3 options attached):

"With this card you or someone you know can have a FREE intro coaching call to get support in overcoming blocks and actualizing your greatest potential."

To schedule, contact:

Fern Halloway, Evolutionary Coach and Facilitator
Fern@[url removed, login to view]
707.514.2893

You might want to check out my website at [url removed, login to view] to see my existing colors as well as the attache flier that I had designed recently.

I'd like to print them on rounded rectangular cards, you can see the specs in the attached template 3.5x2_diecut_business_card___rounded_corners_189+%281%[url removed, login to view]

thanks!

```html
<!DOCTYPE html>
<html lang="en">
<head>
<meta charset="utf-8">
<title>Discover – Coaching Business Card</title>
<link href="https://fonts.googleapis.com/css2?family=Oswald:wght@400;500&family=Fira+Sans+Extra+Condensed:wght@300;400;600;700&display=swap" rel="stylesheet">
<style>
  :root {
    --page: #ffffff;
    --leaf: #a9d66c;
    --leaf-light: #cbe79b;
    --leaf-deep: #93c858;
    --berry: #ad1f5b;
    --white: #ffffff;
    --portrait: #c9a89a;
  }
  * { box-sizing: border-box; margin: 0; padding: 0; }
  html, body { width: 1200px; height: 633px; overflow: hidden; background: var(--page); }
  .canvas { position: relative; width: 1200px; height: 633px; }

  .card {
    position: absolute;
    top: 144px;
    width: 488px;
    height: 299px;
    border-radius: 29px;
    overflow: hidden;
    background: var(--leaf);
  }
  .card--front { left: 96px; }
  .card--back { left: 627px; }

  .card__backdrop {
    position: absolute; inset: 0;
    background:
      radial-gradient(ellipse 70% 90% at 50% 100%, var(--leaf-deep) 0%, transparent 70%),
      radial-gradient(ellipse 60% 80% at 50% 10%, var(--leaf-light) 0%, transparent 75%),
      var(--leaf);
  }

  /* Front */
  .headline {
    position: absolute;
    left: 128px;
    top: 102px;
    width: 230px;
    font-family: "Oswald", sans-serif;
    font-weight: 500;
    font-size: 80px;
    line-height: 1;
    letter-spacing: -1px;
    color: var(--berry);
  }
  .headline__word { display: block; transform: scaleX(0.76); transform-origin: left; white-space: nowrap; }
  .headline__sub {
    display: block;
    margin-top: 2px;
    font-family: "Fira Sans Extra Condensed", sans-serif;
    font-weight: 300;
    font-size: 14px;
    letter-spacing: 0;
    color: var(--white);
    text-align: right;
    white-space: nowrap;
  }

  /* Back */
  .offer {
    position: absolute;
    left: 29px;
    top: 40px;
    width: 300px;
    font-family: "Fira Sans Extra Condensed", sans-serif;
    font-weight: 400;
    font-size: 19px;
    line-height: 33px;
    color: var(--white);
  }
  .offer__line { display: block; white-space: nowrap; }
  .offer__free { color: var(--berry); font-weight: 700; }

  .contact-band {
    position: absolute;
    left: 0; right: 0; bottom: 0;
    height: 92px;
    background: var(--berry);
    font-family: "Fira Sans Extra Condensed", sans-serif;
    color: var(--white);
  }
  .brand-mark {
    position: absolute;
    left: 34px; top: 30px;
    width: 22px; height: 22px;
    border-radius: 50%;
    background: var(--white);
  }
  .contact-band__who { position: absolute; left: 86px; top: 12px; font-size: 13px; line-height: 19px; font-weight: 300; white-space: nowrap; }
  .contact-band__label { font-weight: 600; font-size: 14px; }
  .contact-band__reach { position: absolute; left: 272px; top: 29px; font-size: 13px; line-height: 22px; font-weight: 300; white-space: nowrap; }
  .reach-line { display: flex; align-items: center; gap: 8px; }
  .reach-line svg { width: 12px; height: 12px; fill: none; stroke: var(--white); stroke-width: 1.6; }

  .portrait-frame {
    position: absolute;
    left: 338px; top: 28px;
    width: 146px; height: 146px;
    border-radius: 50%;
    background: var(--berry);
  }
  .portrait {
    position: absolute;
    left: 7px; top: 5px;
    width: 132px; height: 132px;
    border-radius: 50%;
    background: radial-gradient(circle at 45% 40%, #e7cfc4 0%, var(--portrait) 55%, #5a3a33 100%);
  }
</style>
</head>
<body>
<div class="canvas">

  <section class="card card--front">
    <div class="card__backdrop" role="img" aria-label="Soft green lotus petal pattern"></div>
    <h1 class="headline">
      <span class="headline__word">DISCOVER</span>
      <span class="headline__sub">your heart’s deepest calling</span>
    </h1>
  </section>

  <section class="card card--back">
    <div class="card__backdrop" role="img" aria-label="Soft green lotus petal pattern"></div>
    <p class="offer">
      <span class="offer__line">With this card you or someone you know</span>
      <span class="offer__line">can have a <span class="offer__free">FREE</span> intro coaching call to</span>
      <span class="offer__line">get support in overcoming blocks and</span>
      <span class="offer__line">actualizing your greatest potential.</span>
    </p>

    <div class="contact-band">
      <span class="brand-mark"></span>
      <div class="contact-band__who">
        <div class="contact-band__label">To schedule, contact:</div>
        <div>Fern Halloway</div>
        <div>Evolutionary Coach and Facilitator</div>
      </div>
      <div class="contact-band__reach">
        <div class="reach-line">
          <svg viewBox="0 0 12 12"><path d="M2 1.5 L4.2 1.5 L5 4 L3.8 5 Q5 7.3 7 8.2 L8 7 L10.5 7.8 L10.5 10 Q5.5 10.5 1.5 2 Z" fill="#fff" stroke="none"/></svg>
          <span>707.514.2893</span>
        </div>
        <div class="reach-line">
          <svg viewBox="0 0 12 12"><rect x="1" y="2.5" width="10" height="7"/><path d="M1 2.5 L6 6.5 L11 2.5"/></svg>
          <span>Fern@RootedEmber.com</span>
        </div>
      </div>
    </div>

    <div class="portrait-frame">
      <div class="portrait" role="img" aria-label="Headshot of the coach"></div>
    </div>
  </section>

</div>
</body>
</html>
```